Web & Logo Design Project

STOP...please read entire brief before submitting :)
(designers have been submitting random designs)

Global Craft Mobility Network USA seeks new website.
NorvaleArc.example

Who we are: A brand new company that brings top student designers to Los Angeles for the summer to learn English and intern at some of the best design firms in Hollywood.

Clients: Students aged 19-25 and their parents

Objectives: A professional and creative site that communicates design, education, and a 4 star experience.

- Should be professional so that students trust the company
- Should encourage students to apply
- Needs to communicate creativity & design
- Should focus on the professional design studio experience and the location: Los Angeles & Hollywood!

What we need: Logo + Website

Logo should work small as a favicon and large when used on posters.
It should have an icon and the words NORVALE ARC.
Icon should work with and without the words.
Logo can be an abstract shape or a stylized light bulb.
A folder of possible logo ideas can be downloaded below.
Red White & Blue can be used, or stars. Eventually we will add other countries so logo should be able to change accordingly.

Website MUST have an animated slideshow of design pictures and location shots for the landing page. It should give students and idea of what to expect on the program. Please select your favorite pics from all of the photos attached.

Site should also be easy to maintain and optimize.
Should be easy to upload photos and add companies to the company page.

Please submit:

Logo
Landing Page
The Program Page
The Companies Page

Winner of the project will be asked to program the entire site an upload site to the server. We would also like to work with the designer in the future to upload and change the site. The final site will be in 3 languages (French, English, Spanish).

Other sites in our industry:
www.trellimarkcohort.example
www.brightwaveplacements.example

Files Provided:
Web layout in PDF format
Sample photos. (We encourage you to source additional photos.)
Logo examples
Website text in word doc. (coming soon)

If you have any questions please feel free to message us.

Target Market(s)

Students 19-25 and their parents

Industry/Entity Type

Education

Requirements
Must have
• Please use the Web Layout PDF provided and the content doc instead of lorem ipsum or Greek text with random buttons and navigation.

Animated slideshow of project photos on landing page.
Application form, Employer form, contact form
Should not have
• Should not look like an American flag. A nod to the fact that we are bringing students to the US for the summer is great, but this is not a political website. This is a site for designers that want to travel and experience Hollywood.

```html
<!DOCTYPE html>
<html lang="en">
<head>
<meta charset="utf-8">
<title>Hire a Student – NORVALE ARC</title>
<link rel="stylesheet" href="https://fonts.googleapis.com/css2?family=Source+Sans+3:wght@300;400;600;700&display=swap">
<style>
  :root {
    --header-bg: #161616;
    --header-bg-2: #222;
    --nav-text: #c9c9c9;
    --nav-active: #ffffff;
    --logo-text: #d6d6d6;
    --tagline: #d8b4b4;
    --page-bg: #f8f8f8;
    --divider: #3a3a3a;
    --sidebar-bg: #ebebeb;
    --sidebar-frame: #ffffff;
    --accent: #3b7dc8;
    --button: #5f8dcc;
    --heading: #222222;
    --body-text: #5a5a5a;
    --lead-text: #555555;
    --muted: #8a8a8a;
    --required: #d01010;
    --field-border: #e4e4e4;
  }
  * { box-sizing: border-box; margin: 0; padding: 0; }
  html, body { width: 1025px; height: 1200px; overflow: hidden; }
  body {
    position: relative;
    background: var(--page-bg);
    font-family: "Source Sans 3", "Helvetica Neue", Arial, sans-serif;
    color: var(--body-text);
  }

  /* Header */
  .site-header {
    position: absolute; left: 0; top: 0; width: 1025px; height: 211px;
    background: linear-gradient(180deg, var(--header-bg-2), var(--header-bg));
    border-bottom: 6px solid var(--divider);
  }
  .brand {
    position: absolute; left: 56px; top: 52px;
    display: flex; align-items: center; gap: 14px;
  }
  .brand-mark { width: 34px; height: 34px; border-radius: 50%; background: var(--logo-text); }
  .brand-name {
    font-weight: 300; font-size: 62px; letter-spacing: 2px; line-height: 1;
    color: var(--logo-text);
  }
  .tagline {
    position: absolute; left: 622px; top: 94px;
    font-weight: 400; font-size: 36px; letter-spacing: -0.5px;
    color: var(--tagline);
  }
  .main-nav {
    position: absolute; left: 0; top: 165px; width: 1025px; height: 20px;
  }
  .main-nav a {
    position: absolute; top: 0;
    font-size: 13px; color: var(--nav-text); text-decoration: none; text-transform: uppercase;
  }
  .main-nav a.is-active { color: var(--nav-active); }
  .nav-icon {
    position: absolute; top: -3px; width: 24px; height: 24px; border-radius: 50%;
    background: #2a2a2a; display: flex; align-items: center; justify-content: center;
  }

  /* Content panel */
  .content-panel {
    position: absolute; left: 11px; top: 211px; width: 1008px; height: 989px;
    background: var(--page-bg);
  }

  /* Sidebar */
  .partners-sidebar {
    position: absolute; left: 36px; top: 35px; width: 196px; height: 960px;
    background: var(--sidebar-frame); padding: 6px;
  }
  .partners-inner {
    background: var(--sidebar-bg); height: 100%; padding: 18px 18px 0 18px; overflow: hidden;
  }
  .sidebar-title {
    font-size: 17px; font-weight: 400; color: var(--heading); line-height: 20px; letter-spacing: -0.3px;
  }
  .sidebar-title span { color: var(--accent); }
  .partner { margin-top: 22px; }
  .partner + .partner { margin-top: 2px; }
  .partner-name { font-size: 16px; font-weight: 400; color: var(--heading); letter-spacing: -0.3px; line-height: 20px; }
  .partner-desc {
    margin-top: 22px; font-size: 12.5px; line-height: 20.4px; color: var(--body-text);
  }
  .read-more {
    display: flex; align-items: center; gap: 4px; margin-top: 4px; height: 14px;
    font-size: 9.5px; color: var(--muted); text-transform: uppercase;
  }
  .read-more-dot { width: 8px; height: 8px; border-radius: 50%; background: var(--muted); }

  /* Main column */
  .page-title {
    position: absolute; left: 294px; top: 26px;
    font-size: 52px; font-weight: 600; line-height: 54px; color: var(--accent); letter-spacing: 0.5px;
  }
  .lead {
    position: absolute; left: 294px; top: 162px; width: 320px;
    font-size: 19px; line-height: 22px; color: var(--lead-text);
  }
  .hero-photo {
    position: absolute; left: 634px; top: 57px; width: 318px; height: 366px;
    background: radial-gradient(ellipse at 45% 55%, #c7b8a8 0%, #b6a491 45%, rgba(248,248,248,0) 72%);
  }
  .required-note { position: absolute; left: 294px; top: 412px; font-size: 7px; color: var(--body-text); }

  .hire-form { position: absolute; left: 294px; top: 449px; width: 300px; }
  .field { margin-bottom: 22px; }
  .field-label {
    display: block; font-size: 8px; font-weight: 700; letter-spacing: 0.4px; color: var(--heading);
    text-transform: uppercase;
  }
  .field-label em { color: var(--required); font-style: normal; }
  .field-hint { display: block; margin: 5px 0 3px 9px; font-size: 12px; color: var(--body-text); }
  .field-input {
    position: relative; display: block; width: 206px; height: 38px;
    background: #fff; border: 1px solid var(--field-border); border-radius: 2px;
  }
  .field-input::after {
    content: ""; position: absolute; right: 0; top: 0;
    border-top: 6px solid var(--required); border-left: 6px solid transparent;
  }
  .field-select { display: flex; align-items: center; padding-left: 13px; font-size: 13px; color: #333; }
  .field-select::after { display: none; }
  .select-arrow {
    position: absolute; right: 11px; top: 12px; width: 13px; height: 13px;
    border: 1px solid #666; background: #ddd;
  }
  .form-actions { display: flex; gap: 3px; margin-top: 20px; }
  .button {
    width: 116px; height: 49px; background: var(--button); color: #fff; border-radius: 2px;
    font-size: 11px; font-weight: 700; text-transform: uppercase;
    display: flex; align-items: center; justify-content: center; padding-bottom: 10px;
  }
  .button-reset { width: 122px; }
  .pager-next { position: absolute; left: 916px; top: 870px; font-size: 12px; font-weight: 600; color: #555; }
</style>
</head>
<body>
  <header class="site-header">
    <div class="brand">
      <span class="brand-mark"></span>
      <span class="brand-name">NORVALE ARC</span>
    </div>
    <div class="tagline">Design your future.</div>
    <nav class="main-nav">
      <a style="left:101px">Home</a>
      <a style="left:199px">Apply</a>
      <a style="left:299px">Mission</a>
      <a style="left:410px">The Program</a>
      <a class="is-active" style="left:554px">The Companies</a>
      <a style="left:707px">FAQ</a>
      <a style="left:794px">Contact Us</a>
      <span class="nav-icon" style="left:906px">
        <svg width="11" height="11" viewBox="0 0 11 11"><circle cx="5.5" cy="3" r="2.5" fill="#ccc"/><path d="M0.5 11 Q0.5 6 5.5 6 Q10.5 6 10.5 11 Z" fill="#ccc"/></svg>
      </span>
      <span class="nav-icon" style="left:945px">
        <svg width="11" height="11" viewBox="0 0 11 11"><circle cx="4.5" cy="4.5" r="3.2" fill="none" stroke="#ccc" stroke-width="1.8"/><line x1="7" y1="7" x2="10" y2="10" stroke="#ccc" stroke-width="2"/></svg>
      </span>
    </nav>
  </header>

  <main class="content-panel">
    <aside class="partners-sidebar">
      <div class="partners-inner">
        <h3 class="sidebar-title"><span>Sidebar</span> Left (Partners) optional</h3>

        <article class="partner">
          <h4 class="partner-name">Larkfield + Larkfield</h4>
          <p class="partner-desc">Larkfield + Larkfield is a full service advertising agency specializing in branding, design, and internet services for a wide range of fashion, entertainment, and consumer goods companies. At this b...</p>
          <div class="read-more"><span class="read-more-dot"></span>Read more</div>
        </article>

        <article class="partner">
          <h4 class="partner-name">Wide Frame Collective</h4>
          <p class="partner-desc">&nbsp; Wide Frame Collective is an advertising agency specializing in broadcast, interactive and print for the entertainment industry. They create and implement campaigns for many p...</p>
          <div class="read-more"><span class="read-more-dot"></span>Read more</div>
        </article>

        <article class="partner">
          <h4 class="partner-name">Halcyon Venue Group</h4>
          <p class="partner-desc">Halcyon Venue Group runs and manages the hottest nightclubs in Hollywood, like Lanternhall and Echo. Interns will be working with Halcyon's creative director and marketing director developing promotio...</p>
          <div class="read-more"><span class="read-more-dot"></span>Read more</div>
        </article>

        <article class="partner">
          <h4 class="partner-name">Petit Arc Studio</h4>
          <p class="partner-desc">&nbsp; Petit Arc Studio is a full service design studio specializing in print and motion graphics. They create intros for many popular TV series and films as well as</p>
        </article>
      </div>
    </aside>

    <h1 class="page-title">HIRE A<br>STUDENT</h1>
    <p class="lead">Lorem ipsum dolor sit amet, consectetur adipisicing elit, sed do eiusmod tempor incididunt ut labore et dolore magna aliqua, Lorem ipsum dolor sit amet, consectetur adipisicing elit, sed do eiusmod tempor incididunt ut labore et dolore magna aliqua.</p>
    <div class="hero-photo" role="img" aria-label="Photo of a smiling young design student holding a large paintbrush cut-out"></div>

    <p class="required-note">Fields marked with * are required</p>

    <form class="hire-form">
      <div class="field">
        <span class="field-label">Company <em>*</em></span>
        <span class="field-hint">Please select your company name</span>
        <span class="field-input field-select">Please select one<span class="select-arrow"></span></span>
      </div>
      <div class="field">
        <span class="field-label">Representative name <em>*</em></span>
        <span class="field-hint">Please enter your name</span>
        <span class="field-input"></span>
      </div>
      <div class="field">
        <span class="field-label">Email <em>*</em></span>
        <span class="field-hint" style="margin:0 0 3px 0;height:6px"></span>
        <span class="field-input"></span>
      </div>
      <div class="field">
        <span class="field-label">Student's name <em>*</em></span>
        <span class="field-hint">Please enter the name of the student you want to hire.</span>
        <span class="field-input"></span>
      </div>
      <div class="form-actions">
        <span class="button">Send</span>
        <span class="button button-reset">Reset</span>
      </div>
    </form>

    <span class="pager-next">Next &gt;</span>
  </main>
</body>
</html>
```